Natural Light/Organic/Documentary Photography Business

I like a simple, approachable, feminine, earthy/organic feel. Earth/neutral tones, nothing too loud or obnoxious. I like the watercolor look. I don't want anything too trendy or something I'll get tired of after a couple months. As far as colors, I am much more a fan of cream/taupe/blue/green...not a fan of pink or purple at all.

Target Market(s)

Weddings & Families

Industry/Entity Type

Wedding Photography

Contact Information for Business Card

website, email, phone number

Font styles to use
Other font styles liked:
• Horizontes, Gotham

Colors

Designer to choose colors to be used in the design.

Requirements
Must have
• Website: www.meliskaverholt.com
• Phone: 482.319.6047
• Email: tessa@meliskaverholt.com
Nice to have
• I like the watercolor look but its not necessary. I like simple/earthy tones. Nothing too loud or distracting. Simple & feminine without being too girly. I like an approachable/soft feel.
• Instagram: www.instagram.com/meliskaverholtphotography/
Should not have
• NO loud colors or design or pattern. I do not want a photo of a camera or lens or anything cheesy like that.

```html
<!DOCTYPE html>
<html lang="en">
<head>
<meta charset="utf-8">
<title>Meliska Verholt Photography — Business Card</title>
<link rel="stylesheet" href="https://fonts.googleapis.com/css2?family=Cormorant+Garamond:wght@400;500&family=Montserrat:wght@400&display=swap">
<style>
  :root {
    --paper: #fbf7f1;
    --ink: #4e4545;
    --wordmark: #76676a;
    --sage: #a9ad8a;
    --sage-fade: #fbf7f1;
    --taupe: #e6d6c3;
    --olive-tint: #e9e4cf;
  }
  * { margin: 0; padding: 0; box-sizing: border-box; }
  html, body {
    width: 1200px;
    height: 678px;
    overflow: hidden;
    background: var(--paper);
  }
  .card {
    position: relative;
    width: 1200px;
    height: 678px;
    background: var(--paper);
    overflow: hidden;
    font-family: "Cormorant Garamond", Georgia, serif;
    color: var(--ink);
  }
  .art {
    position: absolute;
  }
  .art--left {
    left: 0;
    top: 0;
    width: 360px;
    height: 678px;
    background: linear-gradient(90deg, var(--sage) 0%, var(--sage-fade) 100%);
    opacity: 0.55;
  }
  .art--right {
    left: 560px;
    top: 0;
    width: 640px;
    height: 560px;
    background: radial-gradient(ellipse 70% 65% at 65% 45%, var(--taupe) 0%, var(--olive-tint) 55%, var(--paper) 100%);
  }
  .wordmark__name {
    position: absolute;
    left: 0;
    right: 0;
    top: 228px;
    text-align: center;
    font-size: 112px;
    line-height: 1;
    letter-spacing: 3px;
    font-weight: 400;
    color: var(--wordmark);
  }
  .wordmark__tagline {
    position: absolute;
    left: 0;
    right: 0;
    top: 338px;
    text-align: center;
    font-family: "Montserrat", Arial, sans-serif;
    font-size: 17px;
    line-height: 20px;
    letter-spacing: 12px;
    padding-left: 12px;
    text-transform: uppercase;
    color: var(--wordmark);
  }
  .contact {
    position: absolute;
    left: 0;
    right: 0;
    top: 622px;
    text-align: center;
    font-size: 17px;
    font-variant: small-caps;
    letter-spacing: 0.3px;
    color: var(--ink);
    white-space: nowrap;
  }
  .contact__sep { margin: 0 6px; }
</style>
</head>
<body>
<main class="card">
  <div class="art art--left" role="img" aria-label="Sage-green watercolour leaves along the left edge"></div>
  <div class="art art--right" role="img" aria-label="Soft taupe and olive watercolour washes behind the name"></div>

  <header class="wordmark">
    <div class="wordmark__name">Meliska Verholt</div>
    <div class="wordmark__tagline">Photography</div>
  </header>

  <footer class="contact">
    <span class="contact__item">482.319.6047</span><span class="contact__sep">|</span>
    <span class="contact__item">email: tessa@meliskaverholt.com</span><span class="contact__sep">|</span>
    <span class="contact__item">web: www.meliskaverholt.com</span><span class="contact__sep">|</span>
    <span class="contact__item">Insta: @meliskaverholtphotography</span>
  </footer>
</main>
</body>
</html>
```